Asphalt Driveway Billboard Design

We need a billboard designed for an Asphalt & Concrete Company in Minnesota. We want to advertise Asphalt Driveways on this billboard! Logo is uploaded below. Our website is tamlin-paving.com for more information.

```html
<!DOCTYPE html>
<html lang="en">
<head>
<meta charset="utf-8">
<title>Tamlin Paving &amp; Concrete – Billboard</title>
<link rel="stylesheet" href="https://fonts.googleapis.com/css2?family=Oswald:wght@500;600&family=Montserrat:wght@600;700&display=swap">
<style>
  :root {
    --canvas-bg: #c9dcfb;
    --brand-blue: #3aa6dc;
    --deep-blue: #1c6fc0;
    --navy: #1b3f8f;
    --charcoal: #2b2b2b;
    --white: #ffffff;
  }
  html, body {
    margin: 0;
    width: 1057px;
    height: 1200px;
    overflow: hidden;
    background: var(--canvas-bg);
  }
  .billboard {
    position: absolute;
    left: 40px;
    top: 386px;
    width: 977px;
    height: 428px;
    box-shadow: 0 10px 24px rgba(0,0,0,0.25);
  }
  .billboard svg { display: block; width: 100%; height: 100%; }
  .headline { font-family: "Oswald", sans-serif; font-weight: 600; }
  .tagline, .service { font-family: "Oswald", sans-serif; font-weight: 500; }
  .brand-name, .brand-sub, .contact { font-family: "Montserrat", sans-serif; font-weight: 700; }
</style>
</head>
<body>
<div class="billboard">
  <svg viewBox="0 0 684 300" xmlns="http://www.w3.org/2000/svg">
    <defs>
      <linearGradient id="homeBackdrop" x1="0" y1="0" x2="0" y2="1">
        <stop offset="0" stop-color="#3a3a3a"/>
        <stop offset="1" stop-color="#222222"/>
      </linearGradient>
      <linearGradient id="houseTones" x1="0" y1="0" x2="0" y2="1">
        <stop offset="0" stop-color="#8fc3ef"/>
        <stop offset="0.45" stop-color="#5f8a4c"/>
        <stop offset="0.7" stop-color="#c9b08a"/>
        <stop offset="1" stop-color="#5a5a5a"/>
      </linearGradient>
      <linearGradient id="roadTones" x1="0" y1="0" x2="0" y2="1">
        <stop offset="0" stop-color="#9cc9f0"/>
        <stop offset="0.5" stop-color="#4f8a3e"/>
        <stop offset="1" stop-color="#2c2c2c"/>
      </linearGradient>
      <linearGradient id="garageTones" x1="0" y1="0" x2="0" y2="1">
        <stop offset="0" stop-color="#a7d0f2"/>
        <stop offset="0.5" stop-color="#7f8a96"/>
        <stop offset="1" stop-color="#262626"/>
      </linearGradient>
      <linearGradient id="pillFill" x1="0" y1="0" x2="1" y2="0">
        <stop offset="0" stop-color="var(--brand-blue)"/>
        <stop offset="1" stop-color="var(--deep-blue)"/>
      </linearGradient>
    </defs>

    <rect class="base" width="684" height="300" fill="var(--brand-blue)"/>

    <path class="backdrop-photo" role="img" aria-label="Dimmed photo of a house front behind the headline"
          d="M100 0 H684 V200 Q560 245 420 250 L300 300 H100 Z" fill="url(#homeBackdrop)"/>

    <path class="footer-swoosh" d="M330 300 Q480 240 684 208 V300 Z" fill="var(--brand-blue)"/>
    <path class="footer-panel" d="M372 300 Q500 252 684 222 V300 Z" fill="var(--white)"/>

    <path class="side-panel" d="M0 0 H100 Q84 150 132 300 H0 Z" fill="var(--brand-blue)"/>
    <path class="side-edge" d="M100 0 Q84 150 132 300" fill="none" stroke="var(--white)" stroke-width="3"/>

    <g class="brand">
      <circle cx="55" cy="32" r="13" fill="none" stroke="var(--white)" stroke-width="3"/>
      <text class="brand-name" x="55" y="67" font-size="16" fill="var(--white)" text-anchor="middle">TAMLIN</text>
      <text class="brand-sub" x="55" y="76" font-size="5.2" fill="var(--white)" text-anchor="middle">PAVING &amp; CONCRETE</text>
    </g>

    <g class="photo-circles" stroke="var(--white)" stroke-width="4">
      <circle role="img" aria-label="Photo of a house with a fresh asphalt driveway" cx="211" cy="72" r="98" fill="url(#houseTones)"/>
      <circle role="img" aria-label="Photo of a newly paved palm-lined street" cx="152" cy="215" r="72" fill="url(#roadTones)"/>
      <circle role="img" aria-label="Photo of a grey house with a sealed driveway" cx="282" cy="202" r="66" fill="url(#garageTones)"/>
    </g>

    <text class="headline" x="333" y="65" font-size="38" fill="var(--brand-blue)" textLength="308" lengthAdjust="spacingAndGlyphs">PREMIER ASPHALT</text>
    <text class="headline" x="333" y="107" font-size="30" fill="var(--white)" textLength="308" lengthAdjust="spacingAndGlyphs">&amp; CONCRETE CONTRACTOR</text>

    <rect class="tagline-pill" x="359" y="123" width="258" height="27" rx="13.5" fill="url(#pillFill)"/>
    <text class="tagline" x="488" y="141" font-size="13" fill="var(--white)" text-anchor="middle">YOU DESERVE TO COME HOME TO QUALITY</text>

    <g class="services" fill="var(--white)">
      <path d="M370 169 L380 174 L370 179 L373 174 Z"/>
      <text class="service" x="385" y="178.5" font-size="12">ASPHALT DRIVEWAYS</text>
      <path d="M522 169 L532 174 L522 179 L525 174 Z"/>
      <text class="service" x="538" y="178.5" font-size="12">ASPHALT ADDITIONS</text>
      <path d="M443 192 L453 197 L443 202 L446 197 Z"/>
      <text class="service" x="458" y="201.5" font-size="12">ASPHAL SEALCOATING</text>
    </g>

    <g class="contact-line">
      <circle cx="425" cy="272" r="7" fill="var(--navy)"/>
      <path d="M422 268 q-1 4 3 8 q4 3 6 2 l-1.5 -2 -2 .8 q-2 -1.5 -3.3 -3.3 l.8 -2 Z" fill="var(--white)"/>
      <text class="contact" x="436" y="276" font-size="11.5" fill="var(--navy)">763-555-0142</text>
      <line x1="524" y1="264" x2="524" y2="280" stroke="var(--navy)" stroke-width="1.3"/>
      <circle cx="537" cy="272" r="7" fill="var(--navy)"/>
      <g fill="none" stroke="var(--white)" stroke-width="0.9">
        <circle cx="537" cy="272" r="4.2"/>
        <ellipse cx="537" cy="272" rx="1.8" ry="4.2"/>
        <line x1="532.8" y1="272" x2="541.2" y2="272"/>
      </g>
      <text class="contact" x="548" y="276" font-size="11.5" fill="var(--navy)">tamlin-paving.com</text>
    </g>
  </svg>
</div>
</body>
</html>
```